Holiday Business Card

We are a contracting company who specializes in Earthwork and Demolition. We are looking to have a unique and creative holiday card designed that will include some of the tools and/or machinery that we use. We are okay with using Christmas trees on it, but it must say 'Happy Holidays". It does not need to have trees though, as we are open to new ideas.
We would like to include our logo colors, which are black, orange, and white. Here's our website for reference https://www.brivelcontracting.com/
The card will be a 5" x 7" and one sided (not a folded card). I have included an idea that we liked, but would need to be tailored to our business and not just construction. For instance, we don't use lifts in our business. But this is just a basic idea, and we are open to others.

```html
<!DOCTYPE html>
<html lang="en">
<head>
<meta charset="utf-8">
<title>Happy Holidays – Brivel Contracting, Inc.</title>
<link rel="stylesheet" href="https://fonts.googleapis.com/css2?family=Great+Vibes&family=Source+Sans+3:wght@400&display=swap">
<style>
  :root {
    --ink: #000000;
    --orange: #f7941d;
    --cream: #fbe9cf;
    --rose: #e8505b;
    --pine: #0f3f3f;
    --pine-deep: #0b2f30;
  }
  html, body {
    margin: 0;
    padding: 0;
    width: 857px;
    height: 1200px;
    overflow: hidden;
    background: var(--ink);
  }
  .card {
    position: relative;
    width: 857px;
    height: 1200px;
    background: var(--ink);
    font-family: "Source Sans 3", "Myriad Pro", Arial, sans-serif;
    color: var(--cream);
    overflow: hidden;
  }
  .burst {
    position: absolute;
    top: -70px;
    width: 250px;
    height: 230px;
    border-radius: 50%;
    background: radial-gradient(circle, rgba(251,233,207,0) 30%, rgba(251,233,207,0.45) 55%, rgba(251,233,207,0) 72%);
  }
  .burst--left { left: -75px; }
  .burst--right { right: -75px; }
  .sky {
    position: absolute;
    left: 40px;
    top: 40px;
    width: 777px;
    height: 350px;
  }
  .greeting {
    position: absolute;
    left: 0;
    top: 300px;
    width: 100%;
    margin: 0;
    text-align: center;
    font-family: "Great Vibes", "Brush Script MT", cursive;
    font-weight: 400;
    color: var(--orange);
    font-size: 172px;
    line-height: 170px;
  }
  .greeting__line { display: block; }
  .greeting__line--second { margin-left: 10px; }
  .wish {
    position: absolute;
    left: 0;
    top: 741px;
    width: 100%;
    margin: 0;
    text-align: center;
    font-size: 28px;
    line-height: 37px;
    color: var(--cream);
  }
  .divider {
    position: absolute;
    left: 411px;
    top: 826px;
    width: 42px;
    height: 2px;
    background: var(--rose);
  }
  .trees {
    position: absolute;
    border-radius: 50% 50% 0 0 / 70% 70% 0 0;
  }
  .trees--left {
    left: 0;
    top: 831px;
    width: 240px;
    height: 369px;
    background: linear-gradient(to bottom, rgba(15,63,63,0.35) 0%, var(--pine) 35%, var(--pine-deep) 100%);
  }
  .trees--right {
    right: 0;
    top: 831px;
    width: 240px;
    height: 369px;
    background: linear-gradient(to bottom, rgba(15,63,63,0.35) 0%, var(--pine) 35%, var(--pine-deep) 100%);
  }
  .trees--center {
    left: 206px;
    top: 1016px;
    width: 445px;
    height: 184px;
    background: linear-gradient(to bottom, rgba(247,148,29,0.15) 0%, rgba(15,63,63,0.85) 40%, var(--pine) 100%);
  }
  .brand {
    position: absolute;
    left: 0;
    top: 874px;
    width: 100%;
    text-align: center;
    color: #ffffff;
    font-weight: 400;
  }
  .brand__name {
    display: block;
    font-size: 62px;
    line-height: 60px;
    letter-spacing: 1px;
  }
  .brand__suffix {
    display: block;
    margin-top: 0;
    font-size: 24px;
    line-height: 28px;
    letter-spacing: 1px;
  }
  .website {
    position: absolute;
    left: 0;
    top: 971px;
    width: 100%;
    text-align: center;
    font-size: 21px;
    line-height: 26px;
    color: var(--cream);
  }
</style>
</head>
<body>
  <main class="card">
    <div class="burst burst--left" role="img" aria-label="Cream sunburst ornament in the top left corner"></div>
    <div class="burst burst--right" role="img" aria-label="Cream sunburst ornament in the top right corner"></div>

    <svg class="sky" viewBox="0 0 777 350" aria-hidden="true">
      <g fill="none" stroke="var(--cream)" stroke-width="1.5">
        <circle cx="234" cy="15" r="3"/>
        <circle cx="461" cy="35" r="3"/>
        <circle cx="571" cy="19" r="3"/>
        <circle cx="288" cy="85" r="3"/>
        <circle cx="497" cy="85" r="3"/>
        <circle cx="645" cy="186" r="3"/>
        <circle cx="386" cy="87" r="5"/>
        <circle cx="73" cy="178" r="5"/>
        <circle cx="714" cy="159" r="5"/>
      </g>
      <circle cx="385" cy="144" r="20" fill="var(--orange)"/>
      <circle cx="31" cy="251" r="11" fill="var(--orange)"/>
      <circle cx="137" cy="259" r="14" fill="none" stroke="var(--orange)" stroke-width="2"/>
      <circle cx="660" cy="264" r="5" fill="var(--cream)"/>
      <circle cx="204" cy="199" r="6" fill="none" stroke="var(--rose)" stroke-width="2"/>
      <circle cx="34" cy="335" r="4" fill="none" stroke="var(--rose)" stroke-width="1.5"/>
      <circle cx="752" cy="335" r="4" fill="none" stroke="var(--orange)" stroke-width="1.5"/>
    </svg>

    <h1 class="greeting">
      <span class="greeting__line">Happy</span>
      <span class="greeting__line greeting__line--second">Holidays</span>
    </h1>

    <p class="wish">We wish you a joyful holiday<br>and a happy New Year</p>
    <div class="divider"></div>

    <div class="trees trees--left" role="img" aria-label="Tall teal Christmas tree with cream outline and ornaments"></div>
    <div class="trees trees--right" role="img" aria-label="Tall teal Christmas tree with cream outline and ornaments"></div>
    <div class="trees trees--center" role="img" aria-label="Four small teal Christmas trees with orange outlines and dotted ornaments"></div>

    <div class="brand">
      <span class="brand__name">BRIVEL</span>
      <span class="brand__suffix">CONTRACTING, INC.</span>
    </div>
    <div class="website">www.brivelcontracting.com</div>
  </main>
</body>
</html>
```